Experienced Home remodel service

I'm a home remodeler. I want a catch phrase that clearly describes viewers what kind of work I'm in like the purple phrase on my rough draft idea. I need my website, phone, logo, slogan included. The picture is of my daughter. I want her on it. Be cool if something could be added to her picture like a hard hat or tool belt ect and her picture cut out/background removed. Some kind of background other than plain white for whole picture. I added extra pics of her so pick one

Target Market(s)

Home owners between 30-60

Industry/Entity Type

Home renovation/remodel

Colors

Designer to choose colors to be used in the design.

Requirements
Must have
• Daughters picture incorporated. Logo, phone, website address, slogan,
Nice to have
• See a hardhat or tool belt added to one of my daughters pictures that is chosen to use by designer

```html
<!DOCTYPE html>
<html lang="en">
<head>
<meta charset="utf-8">
<title>Harlow Home Solutions – Billboard</title>
<link rel="stylesheet" href="https://fonts.googleapis.com/css2?family=Montserrat:wght@700;800&family=Oswald:wght@700&family=Poppins:wght@700;800&family=Roboto+Slab:wght@400&display=swap">
<style>
  :root {
    --page-bg: #e6e9ee;
    --board-light: #f2f2f2;
    --board-mid: #e4e4e4;
    --ink: #0d1117;
    --gold: #e0a225;
    --white: #ffffff;
    --photo-top: #d9c2d8;
    --photo-bottom: #c9b3d6;
  }
  * { box-sizing: border-box; margin: 0; padding: 0; }
  html, body { width: 1200px; height: 900px; overflow: hidden; background: var(--page-bg); }
  .billboard {
    position: absolute; left: 40px; top: 177px; width: 1120px; height: 546px;
    background: linear-gradient(135deg, var(--board-light) 0%, var(--board-mid) 55%, var(--board-light) 100%);
    overflow: hidden;
  }
  .accent-gold { position: absolute; left: 0; top: 373px; width: 82px; height: 173px; background: var(--gold); }
  .accent-dark { position: absolute; left: 82px; top: 210px; width: 61px; height: 336px; background: var(--ink); }
  .brand {
    position: absolute; left: 30px; top: 60px; width: 170px;
    display: flex; flex-direction: column; align-items: center; gap: 6px;
  }
  .brand-row { display: flex; align-items: center; gap: 6px; }
  .brand-square { width: 12px; height: 12px; background: var(--ink); flex: none; }
  .brand-name {
    font-family: "Montserrat", sans-serif; font-weight: 800; font-size: 12px;
    letter-spacing: 1px; color: var(--ink); text-transform: uppercase;
  }
  .brand-meta {
    font-family: "Montserrat", sans-serif; font-weight: 700; font-size: 7px;
    letter-spacing: 1.5px; color: var(--ink); text-align: center; line-height: 1.4;
  }
  .hero-photo {
    position: absolute; left: 262px; top: 22px; width: 318px; height: 524px;
    background: linear-gradient(180deg, var(--photo-top) 0%, var(--photo-bottom) 100%);
    border-radius: 150px 150px 0 0;
  }
  .headline {
    position: absolute; right: 48px; top: 52px; width: 480px; text-align: right;
  }
  .headline-lead {
    font-family: "Poppins", sans-serif; font-weight: 700; font-size: 34px;
    color: var(--ink); line-height: 1.1;
  }
  .headline-service {
    font-family: "Oswald", sans-serif; font-weight: 700; font-size: 73px;
    color: var(--gold); line-height: 1; margin-top: 6px; white-space: nowrap;
  }
  .headline-needs {
    font-family: "Poppins", sans-serif; font-weight: 800; font-size: 100px;
    color: var(--ink); line-height: 1; margin-top: -2px; letter-spacing: -1px;
  }
  .tagline-band {
    position: absolute; left: 661px; top: 299px; width: 454px; height: 96px;
    background: var(--gold); padding: 10px 0 0 32px;
  }
  .tagline-name {
    font-family: "Oswald", sans-serif; font-weight: 700; font-size: 35px;
    color: var(--white); line-height: 1.05; text-transform: uppercase; white-space: nowrap;
  }
  .tagline-slogan {
    font-family: "Roboto Slab", serif; font-weight: 400; font-size: 28px;
    color: var(--white); line-height: 1.2; white-space: nowrap;
  }
  .contact { position: absolute; left: 694px; top: 430px; }
  .contact-icon { position: absolute; left: 0; top: 2px; width: 60px; height: 60px; }
  .contact-label {
    position: absolute; left: 70px; top: 6px; white-space: nowrap;
    font-family: "Montserrat", sans-serif; font-weight: 700; font-size: 18px; color: var(--ink);
  }
  .contact-phone {
    position: absolute; left: 70px; top: 24px; white-space: nowrap;
    font-family: "Montserrat", sans-serif; font-weight: 800; font-size: 41px; color: var(--gold);
  }
  .contact-web {
    position: absolute; left: 0; top: 76px; white-space: nowrap;
    font-family: "Montserrat", sans-serif; font-weight: 700; font-size: 19.5px; color: var(--ink);
  }
</style>
</head>
<body>
  <main class="billboard">
    <div class="accent-gold"></div>
    <div class="accent-dark"></div>

    <div class="brand">
      <div class="brand-row">
        <span class="brand-square"></span>
        <span class="brand-name">Harlow Home Solutions</span>
      </div>
      <p class="brand-meta">BUILD. REPAIR. REPLACE.<br>(555) 014 2738</p>
    </div>

    <div class="hero-photo" role="img" aria-label="Cut-out photo of the owner's smiling daughter wearing a yellow hard hat and a lilac puffer jacket, holding a hammer"></div>

    <div class="headline">
      <p class="headline-lead">FOR ALL YOUR</p>
      <p class="headline-service">HOME REMODEL</p>
      <p class="headline-needs">NEEDS</p>
    </div>

    <div class="tagline-band">
      <p class="tagline-name">Harlow Home Solutions</p>
      <p class="tagline-slogan">Build - Repair - Replace</p>
    </div>

    <div class="contact">
      <svg class="contact-icon" viewBox="0 0 60 60" aria-hidden="true">
        <path d="M14 10c3-2 6-1 7 2l4 9c1 2 0 4-2 5l-3 2c2 6 7 11 13 13l2-3c1-2 3-3 5-2l9 4c3 1 4 4 2 7l-3 4c-2 3-6 4-10 3C25 50 10 35 6 22c-1-4 0-8 3-10z" fill="var(--ink)"/>
        <path d="M34 14a14 14 0 0 1 12 12" stroke="var(--ink)" stroke-width="4" fill="none" stroke-linecap="round"/>
        <path d="M35 4a24 24 0 0 1 21 21" stroke="var(--ink)" stroke-width="4" fill="none" stroke-linecap="round"/>
      </svg>
      <p class="contact-label">CALL US TODAY :</p>
      <p class="contact-phone">555-014-2738</p>
      <p class="contact-web">www.harlowhomesolutions.com</p>
    </div>
  </main>
</body>
</html>
```